Homes, Invest in Non-performing loans

We need only 3 web pages, one for the home, one for the content, one for the properties.
The main focus of our business is to offer non performing loans (before foreclosures) to the general public. All the non-performing mortgages will end in a house, an apartment, a store, etc.
Our customers are able to invest from 10,000usd to 1,000,000usd (average 50,000usd).
Our customers' usual focus groups are employees who want second earnings, perceiving the business feeling without outlay time. They look for a solid finance sense corporation that confers them certainty.
Nearly all our clients desire the house, apartment, store, etc. more than the actual earnings.
The name of our company is BRAMLEY
Reason: We value the time and effort you already invest in our project. We realize that we did't come back on some of the doubts requested by the designers. It will be inequitable to the designers who prerequisite our feedback. We also appreciate the comprehension of the community in this postponement.
Reason: Designers,
We really apreciate all the time and effort you put on our project. From the begining we ask for 3 pages, so now we will leave the 10 finalist and provide some extra time to submit the other 2 pages.
We will race the price in 10%
Target Market(s)
Our customers average investors works as employees and want to have a second income or business without spending time. (People from 35 to 50)
Industry/Entity Type
Finance
Requirements
Should not have
- FLASH

```html
<!DOCTYPE html>
<html lang="es">
<head>
<meta charset="utf-8">
<title>BRAMLEY · Remates Hipotecarios</title>
<link href="https://fonts.googleapis.com/css2?family=Open+Sans:wght@400;600;700&family=Marcellus&display=swap" rel="stylesheet">
<style>
  :root{
    --black:#0b0b0b;
    --page-grey:#e6e6e6;
    --white:#ffffff;
    --olive:#7f7b22;
    --olive-dark:#6a6619;
    --sky:#3cb4e7;
    --orange:#e8800a;
    --charcoal:#3d3b3c;
    --slate:#3f4144;
    --panel:#ececec;
    --footer-bar:#444444;
    --text-light:#f4f4f4;
  }
  *{box-sizing:border-box;margin:0;padding:0}
  html,body{width:1200px;height:1045px;overflow:hidden}
  body{
    position:relative;
    background:var(--black);
    font-family:Arial,"Helvetica Neue",sans-serif;
    color:var(--white);
  }
  .abs{position:absolute}

  /* top contact bar */
  .topbar{left:0;top:0;width:1200px;height:37px;background:var(--black);border-bottom:1px solid #333}
  .contact{top:9px;font-size:15px;display:flex;align-items:center;gap:8px;color:#fff}
  .contact.email{left:765px;font-weight:700;font-family:"Open Sans",sans-serif}
  .contact.phone{left:953px;font-size:14px}

  /* header band */
  .header-band{
    left:0;top:38px;width:1200px;height:443px;
    background-color:var(--page-grey);
    background-image:radial-gradient(circle,#cfcfcf 1px,transparent 1.3px);
    background-size:4px 4px;
  }
  .brand{left:76px;top:60px;display:flex;align-items:center;gap:10px}
  .brand-mark{width:30px;height:30px;background:var(--olive)}
  .brand-name{font-family:"Open Sans",sans-serif;font-weight:700;font-size:38px;color:#2b2b2b;letter-spacing:-1px;line-height:1}
  .brand-tag{left:77px;top:148px;font-family:"Open Sans",sans-serif;font-size:8px;letter-spacing:1.6px;color:#333}

  .social{top:69px;width:36px;height:36px;border-radius:50%}
  .social.one{left:1046px;background:radial-gradient(circle at 40% 35%,#8fdcf6,#2aa4d8)}
  .social.two{left:1091px;background:radial-gradient(circle at 40% 35%,#4e8be0,#13488f)}

  .main-nav{left:545px;top:113px;height:44px;display:flex;border-radius:3px;overflow:hidden;background:var(--olive)}
  .main-nav a{
    display:flex;align-items:center;justify-content:center;height:100%;
    font-family:"Open Sans",sans-serif;font-weight:600;font-size:14.5px;color:#fff;text-decoration:none;
    border-left:1px solid var(--olive-dark);
  }
  .main-nav a.active{background:var(--sky);color:#0d2b3e;font-weight:700;border-left:none}

  /* content sheet */
  .sheet{left:77px;top:166px;width:1053px;height:790px;background:var(--white);box-shadow:0 0 4px rgba(0,0,0,.3)}

  .hero{left:89px;top:179px;width:1030px;height:302px;overflow:hidden}
  .hero-photo{position:absolute;inset:0;background:linear-gradient(180deg,#9fdcf3 0%,#cdeefa 45%,#d9dcdc 70%,#8d8f8e 100%)}
  .hero-caption{
    position:absolute;left:233px;top:203px;width:747px;height:99px;
    background:rgba(40,40,40,.78);
    display:flex;align-items:center;justify-content:center;
    font-family:"Marcellus",serif;font-size:34px;letter-spacing:2px;color:#fff;
  }
  .hero-arrow{top:310px;width:52px;height:52px;border-radius:50%;background:radial-gradient(circle at 50% 35%,#c9cfd3,#7e8489);border:2px solid #e9eef0}
  .hero-arrow.prev{left:102px}
  .hero-arrow.next{left:1052px}
  .hero-arrow svg{position:absolute;left:14px;top:14px}

  /* feature cards */
  .card{top:518px;width:307px;height:151px;border-radius:8px;overflow:hidden;padding:14px 15px}
  .card.services{left:111px;background:var(--orange)}
  .card.benefits{left:448px;background:var(--olive)}
  .card.auctions{left:783px;background:var(--sky)}
  .card h2{font-family:"Open Sans",sans-serif;font-weight:700;font-size:17px;padding-bottom:8px;border-bottom:1px dashed rgba(255,255,255,.5);margin-bottom:9px}
  .card p{font-size:12.3px;line-height:15px;position:relative;z-index:1;width:274px}
  .card p.lead{font-weight:700;margin-bottom:14px}
  .card-corner{position:absolute;right:0;bottom:0}
  .card-btn{position:absolute;right:10px;bottom:9px;width:36px;height:36px;border-radius:50%;background:#fff;display:flex;align-items:center;justify-content:center;box-shadow:0 1px 2px rgba(0,0,0,.4)}

  /* promo panel */
  .promo{left:112px;top:697px;width:643px;height:232px;background:var(--charcoal);border-radius:3px;padding:18px 20px}
  .promo h2{font-family:"Open Sans",sans-serif;font-weight:700;font-size:17px;margin-bottom:14px}
  .promo p{font-size:12.8px;line-height:16.5px;width:340px;margin-bottom:14px}
  .promo-photo{left:469px;top:713px;width:271px;height:190px;background:linear-gradient(180deg,#cfd2d4 0%,#b9bcbd 55%,#5e8ea1 80%,#3f6f86 100%)}
  .pager{left:363px;top:876px;display:flex;gap:7px}
  .pager span{width:26px;height:26px;border-radius:50%;background:#fff;color:#333;font-weight:700;font-size:16px;display:flex;align-items:center;justify-content:center}

  /* login panel */
  .login{left:782px;top:697px;width:309px;height:232px;background:var(--panel);border-radius:8px;border:1px solid #d5d5d5}
  .login-head{position:absolute;left:0;top:10px;width:292px;height:46px;background:var(--olive);clip-path:polygon(0 0,94% 0,100% 50%,94% 100%,0 100%)}
  .login-head h2{font-family:"Open Sans",sans-serif;font-weight:700;font-size:16px;line-height:46px;padding-left:15px;color:#fff}
  .login-rule{position:absolute;left:12px;right:12px;top:76px;border-top:1px dashed #c8c8c8}
  .field{position:absolute;left:12px;width:280px;height:34px;border:1px solid #d2d2d2;border-radius:5px;background:linear-gradient(#f6f6f6,#e9e9e9);font-size:13px;color:#555;padding:9px 10px;font-family:"Open Sans",sans-serif}
  .btn-enter{position:absolute;left:12px;top:188px;width:77px;height:29px;border-radius:4px;background:linear-gradient(#8a8625,#6a6619);color:#fff;font-family:"Open Sans",sans-serif;font-weight:700;font-size:13px;display:flex;align-items:center;justify-content:center}

  /* footer */
  .footer-nav{left:0;top:968px;width:1200px;display:flex;justify-content:center;font-family:"Open Sans",sans-serif;font-size:13px}
  .footer-nav a{color:#fff;text-decoration:none;padding:0 27px;border-left:1px solid #fff;line-height:18px}
  .footer-nav a:first-child{border-left:none}
  .footer-bar{left:0;top:1007px;width:1200px;height:38px;background:var(--footer-bar);display:flex;align-items:center;justify-content:center;font-family:"Open Sans",sans-serif;font-size:12.5px;color:#e8e8e8}
</style>
</head>
<body>

<div class="abs topbar"></div>
<div class="abs contact email">
  <svg width="22" height="16" viewBox="0 0 22 16"><rect x="1" y="1" width="20" height="14" fill="none" stroke="#fff" stroke-width="1.5"/><path d="M1 1 11 9 21 1" fill="none" stroke="#fff" stroke-width="1.5"/></svg>
  ventas@bramley.mx
</div>
<div class="abs contact phone">
  <svg width="18" height="18" viewBox="0 0 18 18"><rect width="18" height="18" rx="3" fill="#fff"/><path d="M6 4c-1 1-1.5 2-.8 4 .8 2.3 2.6 4.3 4.8 5.5 1.5.7 2.4.4 3.2-.4l-1.6-1.8-1.4.7c-1.3-.7-2.4-1.9-3-3.2l.8-1.3z" fill="#111"/></svg>
  VENTAS (55) 4100 - 3800
</div>

<header class="abs header-band"></header>
<div class="abs brand"><span class="brand-mark"></span><span class="brand-name">BRAMLEY</span></div>
<div class="abs brand-tag">REMATES HIPOTECARIOS</div>

<span class="abs social one"></span>
<span class="abs social two"></span>

<nav class="abs main-nav">
  <a class="active" href="#" style="width:108px">REMATES</a>
  <a href="#" style="width:163px">QUIENES SOMOS</a>
  <a href="#" style="width:122px">CONTATTO</a>
  <a href="#" style="width:97px">ACCESO</a>
  <a href="#" style="width:95px">INICIO</a>
</nav>

<main class="abs sheet"></main>

<section class="abs hero">
  <div class="hero-photo" role="img" aria-label="Fotografía de una casa moderna blanca con techo de teja bajo cielo azul"></div>
  <div class="hero-caption">ES UNA INVERSIÓN Y UNA CASA</div>
</section>
<span class="abs hero-arrow prev"><svg width="20" height="20" viewBox="0 0 20 20"><path d="M13 3 6 10l7 7" fill="none" stroke="#2f3438" stroke-width="4"/></svg></span>
<span class="abs hero-arrow next"><svg width="20" height="20" viewBox="0 0 20 20"><path d="M7 3l7 7-7 7" fill="none" stroke="#2f3438" stroke-width="4"/></svg></span>

<article class="abs card services">
  <h2>SERVICIOS</h2>
  <p>Análisis: Estudios de viabilidad de la Cesión de derechos.Tranquilidad: Nos encargamos de realizar todos los procesos del juicio hasta la escrituración de la propiedad;</p>
  <svg class="card-corner" width="92" height="92" viewBox="0 0 92 92"><polygon points="92,0 92,92 0,92" fill="var(--slate)"/></svg>
  <span class="card-btn"><svg width="14" height="14" viewBox="0 0 14 14"><path d="M4 2l5 5-5 5" fill="none" stroke="#333" stroke-width="3"/></svg></span>
</article>

<article class="abs card benefits">
  <h2>BENIFICIOS</h2>
  <p class="lead">ES UNA INVERSION Y UNA CASA.</p>
  <p>Comprar un Remate Hipotecario en BRAMLEY®, es una excelente forma de inversión de bajo</p>
  <svg class="card-corner" width="92" height="92" viewBox="0 0 92 92"><polygon points="92,0 92,92 0,92" fill="var(--slate)"/></svg>
  <span class="card-btn"><svg width="14" height="14" viewBox="0 0 14 14"><path d="M4 2l5 5-5 5" fill="none" stroke="#333" stroke-width="3"/></svg></span>
</article>

<article class="abs card auctions">
  <h2>REMATES</h2>
  <p>Al contratar con nosotros tu obtienes una Cesión de Derechos con la garantía de la propiedad que elijas, cuya ejecución la lleva a cabo BRAMLEY® a través del remate judicial.</p>
  <svg class="card-corner" width="92" height="92" viewBox="0 0 92 92"><polygon points="92,0 92,92 0,92" fill="var(--slate)"/></svg>
  <span class="card-btn"><svg width="14" height="14" viewBox="0 0 14 14"><path d="M4 2l5 5-5 5" fill="none" stroke="#333" stroke-width="3"/></svg></span>
</article>

<section class="abs promo">
  <h2>ES UNA INVERSION Y UNA CASA</h2>
  <p>Comprar un Remate Hipotecario en BRAMLEY®, es una excelente forma de inversión de bajo costo y alta utilidad, con la garantía de una casa. Podrás adquirir un inmueble ahorrando hasta un 60% de su valor comercial.</p>
  <p>&nbsp;En BRAMLEY® tu inversión se documenta ante Notario Público, con el respaldo y compromiso de profesionales.</p>
</section>
<div class="abs promo-photo" role="img" aria-label="Ilustración de una casa moderna con alberca"></div>
<div class="abs pager"><span>1</span><span>2</span><span>3</span></div>

<section class="abs login">
  <div class="login-head"><h2>FICHAS</h2></div>
  <svg style="position:absolute;left:245px;top:16px" width="34" height="34" viewBox="0 0 34 34"><circle cx="24" cy="10" r="7" fill="#d8d8d8" stroke="#999"/><path d="M19 15 5 29l3 3 2-2 2 2 3-3-2-2 9-9" fill="#d8d8d8" stroke="#999"/></svg>
  <div class="login-rule"></div>
  <div class="field" style="top:95px">Usuario :</div>
  <div class="field" style="top:138px">Password :</div>
  <div class="btn-enter">Entrar</div>
</section>

<nav class="abs footer-nav">
  <a href="#">Remates</a><a href="#">quienes somos</a><a href="#">Contatto</a><a href="#">acceso</a><a href="#">inicio</a>
</nav>
<footer class="abs footer-bar">© 2012 &nbsp;All Rights Reserved. &nbsp;&nbsp;Privacy Policy/ &nbsp;Terms of Use</footer>

</body>
</html>
```